Billboard For Marcus Delvane

Need a Billboard 8ft. High x 16ft. Long. Ive attached a former billboard and looking for the same thing just updated with:
Wardens Guild Award Logo - 2020, 2022
Summit Lantern award Logo - 2022

Thanks.

```html
<!DOCTYPE html>
<html lang="en">
<head>
<meta charset="utf-8">
<title>Billboard – Marcus Delvane</title>
<link rel="stylesheet" href="https://fonts.googleapis.com/css2?family=Poppins:ital,wght@0,500;0,600;0,700;0,800;1,800&family=Oswald:wght@300;400&display=swap">
<style>
  :root{
    --stage:#a8a8a8;
    --paper:#ffffff;
    --ink:#0d0d0d;
    --band:#262626;
    --red:#ee0f0f;
    --red-deep:#d80000;
    --grey-text:#333333;
    --photo-top:#d9c2b4;
    --photo-mid:#e7c5b2;
    --photo-low:#3552a6;
  }
  *{margin:0;padding:0;box-sizing:border-box;}
  html,body{width:915px;height:1200px;overflow:hidden;background:var(--stage);}
  .canvas{position:relative;width:915px;height:1200px;background:var(--stage);}
  .billboard{
    position:absolute;left:60px;top:401px;width:795px;height:398px;
    background:var(--paper);overflow:hidden;
    box-shadow:0 10px 24px rgba(0,0,0,.28);
    font-family:"Poppins",sans-serif;
  }
  .accent-block{position:absolute;left:687px;top:0;width:108px;height:251px;background:linear-gradient(180deg,var(--red-deep),var(--red));}
  .headline{position:absolute;font-weight:800;font-style:italic;color:var(--ink);line-height:1;white-space:nowrap;}
  .headline.buying{left:27px;top:20px;font-size:71px;letter-spacing:-4px;}
  .headline.selling{left:22px;top:89px;font-size:73px;letter-spacing:-2px;}
  .headline.call{left:394px;top:89px;font-size:73px;letter-spacing:-2px;color:var(--red);}
  .or-badge{position:absolute;left:343px;top:31px;width:56px;height:56px;border-radius:50%;background:var(--red);color:#fff;font-weight:800;font-style:italic;font-size:24px;display:flex;align-items:center;justify-content:center;letter-spacing:-1px;}
  .info-band{position:absolute;left:0;top:171px;width:795px;height:138px;background:var(--band);}
  .agent-name{position:absolute;left:28px;top:182px;color:#fff;font-weight:700;font-size:33px;line-height:1.1;white-space:nowrap;}
  .agent-title{position:absolute;left:29px;top:228px;width:301px;height:21px;background:var(--red);color:#fff;font-weight:500;font-size:16px;letter-spacing:3.3px;line-height:21px;padding-left:5px;white-space:nowrap;}
  .agent-phone{position:absolute;left:28px;top:253px;display:flex;align-items:center;gap:7px;color:#fff;font-weight:600;font-size:41px;line-height:1;white-space:nowrap;}
  .phone-icon{width:31px;height:31px;}
  .divider{position:absolute;left:342px;top:193px;width:3px;height:96px;background:var(--red);}
  .tagline{position:absolute;left:359px;top:189px;color:#fff;font-weight:600;font-size:31px;line-height:32px;white-space:nowrap;}
  .portrait{position:absolute;left:580px;top:32px;width:215px;height:366px;}
  .footer-row{position:absolute;left:0;top:318px;width:570px;height:70px;}
  .brand{position:absolute;left:29px;top:21px;display:flex;align-items:center;gap:6px;}
  .brand-square{width:14px;height:14px;background:var(--red);}
  .brand-name{font-weight:700;font-size:16px;color:var(--ink);letter-spacing:.3px;white-space:nowrap;}
  .award{position:absolute;top:9px;display:flex;align-items:center;gap:4px;}
  .award.summit{left:186px;}
  .award.wardens{left:320px;top:6px;}
  .award-seal{border-radius:50%;flex:none;}
  .award.summit .award-seal{width:30px;height:30px;background:#1c1c1c;}
  .award.wardens .award-seal{width:40px;height:40px;background:#fff;border:2px solid #1c1c1c;box-shadow:inset 0 0 0 5px #fff,inset 0 0 0 20px #1c1c1c;}
  .award-text{font-family:"Oswald",sans-serif;color:var(--grey-text);line-height:1;white-space:nowrap;}
  .award-text .org{display:block;font-family:"Poppins",sans-serif;font-size:6px;font-weight:500;margin-bottom:2px;}
  .award-text .title{display:block;font-weight:300;font-size:15px;}
  .award.wardens .award-text .title{font-weight:400;font-size:12px;}
  .award-text .years{display:block;font-weight:400;font-size:10px;margin-top:1px;}
  .award-text .note{display:block;font-family:"Poppins",sans-serif;font-size:4.5px;margin-top:2px;}
  .social{position:absolute;top:22px;left:446px;display:flex;gap:6px;align-items:center;}
  .social-item{display:flex;align-items:center;gap:3px;font-size:8px;font-weight:600;color:var(--ink);white-space:nowrap;}
  .social-dot{width:14px;height:14px;border-radius:50%;background:var(--red);}
</style>
</head>
<body>
<div class="canvas">
  <section class="billboard">
    <div class="accent-block"></div>

    <div class="headline buying">BUYING</div>
    <div class="or-badge">OR</div>
    <div class="headline selling">SELLING?</div>
    <div class="headline call">CALL</div>

    <div class="info-band"></div>
    <div class="agent-name">MARCUS DELVANE</div>
    <div class="agent-title">SALES REPRESENTATIVE</div>
    <div class="agent-phone">
      <svg class="phone-icon" viewBox="0 0 32 32" aria-hidden="true">
        <circle cx="16" cy="16" r="16" fill="#ee0f0f"/>
        <path d="M11 8.5c.8-.5 1.7-.3 2.2.5l1.6 2.6c.4.7.3 1.5-.3 2l-1.3 1.1c.9 2 2.4 3.6 4.4 4.6l1.1-1.3c.5-.6 1.4-.7 2-.3l2.6 1.6c.8.5 1 1.4.5 2.2l-.9 1.5c-.6 1-1.8 1.4-2.9 1.1-5.3-1.6-9.2-5.6-10.7-10.9-.3-1.1.1-2.3 1.1-2.9z" fill="#fff"/>
      </svg>
      <span>613.555.0148</span>
    </div>
    <div class="divider"></div>
    <div class="tagline">Focused,<br>Driven, And<br>Experienced!</div>

    <svg class="portrait" viewBox="0 0 215 366" preserveAspectRatio="none" role="img" aria-label="Portrait photo of the sales representative">
      <defs>
        <linearGradient id="portraitTone" x1="0" y1="0" x2="0" y2="1">
          <stop offset="0" stop-color="#d9c2b4"/>
          <stop offset=".5" stop-color="#e7c5b2"/>
          <stop offset=".7" stop-color="#3552a6"/>
          <stop offset="1" stop-color="#2d4592"/>
        </linearGradient>
      </defs>
      <rect width="215" height="366" fill="url(#portraitTone)"/>
    </svg>

    <div class="footer-row">
      <div class="brand">
        <span class="brand-square"></span>
        <span class="brand-name">CROWN HEARTH</span>
      </div>
      <div class="award summit">
        <span class="award-seal"></span>
        <span class="award-text">
          <span class="org">CROWN HEARTH</span>
          <span class="title">SUMMIT LANTERN</span>
          <span class="title">AWARD 2022</span>
        </span>
      </div>
      <div class="award wardens">
        <span class="award-seal"></span>
        <span class="award-text">
          <span class="org">CROWN HEARTH</span>
          <span class="title">WARDENS GUILD</span>
          <span class="years">2020, 2022</span>
          <span class="note">NATIONAL TOP 1%</span>
        </span>
      </div>
      <div class="social">
        <span class="social-item"><span class="social-dot"></span>Linkhall</span>
        <span class="social-item"><span class="social-dot"></span>Snapvale</span>
      </div>
    </div>
  </section>
</div>
</body>
</html>
```